My garage customisation company needs a business card

I need a business card design for my company "Shed Mavens"
I provide fully customised garage solutions for your previously cluttered, waste of space. My logo was just completed and can be provided if needed. I need the card to be clean, classy and eye catching.
Thank you

Target Market(s)

Men and Woman Home Owners

Industry/Entity Type

Business

Contact Information for Business Card

Rupert Dunwell
rupe@shedmavens.example
shedmavens.example

It's Time To Take Back Your Garage... From simple storage solutions to fully customised from the floor up, we've got you covered.

Requirements
Must have
• Logo
• Name
• Email Address
• Website
• Brief Description of what we do
Nice to have
• Back ground picture of Before and After

```html
<!DOCTYPE html>
<html lang="en">
<head>
<meta charset="utf-8">
<title>Shed Mavens — Business Card</title>
<link rel="stylesheet" href="https://fonts.googleapis.com/css2?family=Open+Sans:wght@400;600;700;800&display=swap">
<style>
  :root {
    --page-bg: #eeeeee;
    --card-dark: #1f1f1f;
    --card-dark-light: #333333;
    --brand-orange: #e8792a;
    --band-orange-deep: #dd6218;
    --band-orange-light: #ef8a35;
    --ink-dark: #2a2a2a;
    --ink-light: #ffffff;
    --ink-muted: #d4d4d4;
  }
  * { box-sizing: border-box; margin: 0; padding: 0; }
  html, body {
    width: 1200px;
    height: 864px;
    overflow: hidden;
    background: var(--page-bg);
    font-family: "Open Sans", Arial, sans-serif;
  }
  .canvas {
    position: relative;
    width: 1200px;
    height: 864px;
    display: flex;
    align-items: center;
    justify-content: center;
    gap: 40px;
  }
  .card {
    position: relative;
    width: 540px;
    height: 310px;
    overflow: hidden;
    box-shadow: 0 10px 24px rgba(0,0,0,0.18);
    background: radial-gradient(ellipse at 50% 35%, var(--card-dark-light) 0%, var(--card-dark) 70%);
  }
  .brand {
    display: flex;
    align-items: center;
    justify-content: center;
    gap: 10px;
  }
  .brand-mark {
    width: 18px;
    height: 18px;
    background: var(--brand-orange);
  }
  .brand-name {
    font-weight: 800;
    color: var(--brand-orange);
    text-transform: uppercase;
    letter-spacing: 0.04em;
  }

  /* front */
  .card-front .brand { position: absolute; top: 46px; left: 0; right: 0; }
  .card-front .brand-name { font-size: 34px; }
  .tagline {
    position: absolute;
    top: 110px;
    left: 0; right: 0;
    text-align: center;
    color: var(--ink-light);
  }
  .tagline-head {
    font-weight: 700;
    font-size: 17px;
    letter-spacing: 0.04em;
    text-transform: uppercase;
  }
  .tagline-sub {
    margin-top: 4px;
    font-size: 11px;
    color: var(--ink-muted);
    line-height: 1.35;
  }
  .contact-band {
    position: absolute;
    left: 0; right: 0; bottom: 0;
    height: 118px;
    background: linear-gradient(120deg, var(--band-orange-deep) 0%, var(--band-orange-light) 100%);
    padding: 28px 40px 0;
    color: var(--ink-dark);
  }
  .contact-name {
    font-weight: 600;
    font-size: 24px;
    letter-spacing: 0.14em;
    text-transform: uppercase;
  }
  .contact-email {
    margin-top: 4px;
    font-size: 15px;
  }

  /* back */
  .card-back .brand { position: absolute; top: 112px; left: 0; right: 0; }
  .card-back .brand-name { font-size: 42px; }
  .back-url {
    position: absolute;
    top: 190px;
    left: 0; right: 0;
    text-align: center;
    font-weight: 700;
    font-size: 17px;
    color: var(--brand-orange);
    letter-spacing: 0.02em;
  }
</style>
</head>
<body>
  <main class="canvas">
    <section class="card card-front" aria-label="Business card front">
      <div class="brand">
        <span class="brand-mark"></span>
        <span class="brand-name">Shed Mavens</span>
      </div>
      <div class="tagline">
        <p class="tagline-head">It's time to take back your garage...</p>
        <p class="tagline-sub">From simple storage solutions to fully customised from the floor up.<br>we've got you covered.</p>
      </div>
      <div class="contact-band">
        <p class="contact-name">Rupert Dunwell</p>
        <p class="contact-email">rupe@shedmavens.example</p>
      </div>
    </section>

    <section class="card card-back" aria-label="Business card back">
      <div class="brand">
        <span class="brand-mark"></span>
        <span class="brand-name">Shed Mavens</span>
      </div>
      <p class="back-url">www.shedmavens.example</p>
    </section>
  </main>
</body>
</html>
```